Lorna Tess Tresses Fancy Business Card’s

I want my business cards to be elite, original and very classy. I want the business cards to match the colors of my logo and to match the design posted. I would love the design of the picture I posted

I want the card all white .
The dripping on the top of the card I want it to match the pink color in my logo that’s also posted .
I need my logo on the business card !
I need my Instagram- @lorna.tess.tresses__
And my phone number - 582 907 3365

Target Market(s)

My target market is young woman age 23 to older woman to the age of 65
I want both older and younger women to love my design . I don’t want any cheap looking business cards

Industry/Entity Type

Hair And Beauty

Contact Information for Business Card

Add my logo
Add my Instagram- @lorna.tess.tresses__
My number - 582 907 3365
My website- www.lornatesstresses.example

Font styles to use
Serif
Script

Colors
ffffff
e667a6
e34298

Requirements
Must have
• The business cards must have my logo, my number , my website, and my Instagram!
Nice to have
• Nice to have glitter words that match my logo
• The business cards must look classy and mature
• I want them to be very unique!!
Should not have
• Should not have any colors that doesn’t match my logo ! This is very important! Please

```html
<!DOCTYPE html>
<html lang="en">
<head>
<meta charset="utf-8">
<title>Lorna Tess Tresses — Business Card</title>
<link href="https://fonts.googleapis.com/css2?family=Montserrat:wght@300;400&display=swap" rel="stylesheet">
<style>
  :root {
    --backdrop: #ececee;
    --card: #ffffff;
    --pink: #e34298;
    --pink-soft: #e667a6;
    --ink: #6e6e6e;
    --hairline: #f1d3e3;
  }
  * { margin: 0; padding: 0; box-sizing: border-box; }
  html, body {
    width: 1200px; height: 900px; overflow: hidden;
    background: var(--backdrop);
    font-family: "Montserrat", sans-serif;
  }
  .sheet {
    width: 1200px; height: 900px;
    display: flex; flex-direction: column;
    align-items: center; justify-content: center; gap: 44px;
  }
  .card {
    position: relative;
    width: 700px; height: 400px;
    background: var(--card);
    box-shadow: 0 12px 32px rgba(0,0,0,0.10);
    overflow: hidden;
  }
  .card::after {
    content: "";
    position: absolute; inset: 18px;
    border: 1px solid var(--hairline);
    pointer-events: none;
  }

  /* Front: brand name */
  .brand-mark {
    position: absolute; inset: 0;
    display: flex; flex-direction: column;
    align-items: center; justify-content: center; gap: 22px;
  }
  .brand-dot {
    width: 12px; height: 12px; border-radius: 50%;
    background: var(--pink);
  }
  .brand-name {
    font-weight: 300;
    color: var(--pink);
    font-size: 40px;
    letter-spacing: 12px;
    text-transform: uppercase;
    text-align: center;
    line-height: 1.45;
    padding-left: 12px;
  }

  /* Back: contact details */
  .contact {
    position: absolute; inset: 0;
    display: flex; flex-direction: column;
    align-items: center; justify-content: center; gap: 26px;
  }
  .contact-name {
    font-weight: 300; font-size: 15px;
    letter-spacing: 8px; text-transform: uppercase;
    color: var(--pink); padding-left: 8px;
  }
  .contact-rule { width: 60px; height: 1px; background: var(--pink-soft); }
  .contact-list {
    list-style: none;
    font-weight: 300; font-size: 19px; color: var(--ink);
    line-height: 1.7; letter-spacing: 0.5px;
    text-align: center;
  }
  .contact-line .label { color: var(--pink); margin-right: 6px; }
  .contact-line .accent { color: var(--pink); }
</style>
</head>
<body>
  <main class="sheet">
    <section class="card card--back" aria-label="Card back with contact details">
      <div class="contact">
        <p class="contact-name">Lorna Tess Tresses</p>
        <span class="contact-rule" aria-hidden="true"></span>
        <ul class="contact-list">
          <li class="contact-line"><span class="label">P:</span>582 907 3365</li>
          <li class="contact-line"><span class="label">I:</span>@lorna.tess.tresses__</li>
          <li class="contact-line"><span class="label">W:</span>www.<span class="accent">lornatesstresses</span>.example</li>
        </ul>
      </div>
    </section>

    <section class="card card--front" aria-label="Card front with brand name">
      <div class="brand-mark">
        <span class="brand-dot" aria-hidden="true"></span>
        <span class="brand-name">Lorna Tess<br>Tresses</span>
      </div>
    </section>
  </main>
</body>
</html>
```